The Nine Gates for Tablet Reliance - Contemporary Book Cover Design

The Nine Gates for Tablet Reliance was published in March 2019 and is available on Brimora and other platforms now. However, I am not happy with the cover.  It's a good design in some ways - I thought it would stand out and be easily recognizable. But I don't really like the color scheme and feel that a self-help book should probably use some lighter colors and that the red is too strident. The color scheme carries over into other marketing materials like the website, social media, etc. and I don't like the red and black scheme for these purposes.
It's not essential that the cover contain an endorsement like the current one but it could. Here are some endorsements:
“A must-read for anyone who is addicted to or thinks they may have a problem with digital technology. This eloquent work will also be useful to academics and clinicians exploring potential solutions. The author recognizes the similarities between smartphone addiction and other addictions, and logically applies one of the most effective known solutions for addiction - The Nine Gates.”
-- Dale Wickersham: Noted Interventionist, Keynote Speaker and Addiction Visionary
“If you suffer from digital addiction, I strongly encourage you to use this book as your road map to get you back to the real world.”
-- Thomas Quillard, Founder of Online Channel Monitor.
The back cover would have the new design / color scheme, but can have similar text, bio, author image, etc. Or we could include the endorsements there and shorten the other text.
As for the cover it could be stylized, or an image, a partial image, or whatever. I am open to suggestions. Think about what would be inviting for a person searching for help with moderating their smartphone use.
Let's add a subtitle as well "An Inner Journey to Balanced Tablet Habits"
Here is a link to the book:
https://www.brimora.example/Nine-Gates-Tablet-Reliance/dp/4086213590

Target Market(s)
General, since this issue affects almost everyone.
Colors
Designer to choose colors to be used in the design.
Look and feel

```html
<!DOCTYPE html>
<html lang="en">
<head>
<meta charset="utf-8">
<title>The Nine Gates for Tablet Reliance — Cover</title>
<link rel="stylesheet" href="https://fonts.googleapis.com/css2?family=Luckiest+Guy&family=Montserrat:wght@500;600&family=Jost:ital,wght@1,400;1,600&display=swap">
<style>
  :root {
    --stage: #8fc48a;
    --paper: #f2f2f2;
    --teal: #12a1a8;
    --teal-soft: #6fbfc3;
    --teal-deep: #0e8f96;
    --ink: #1c1c1c;
    --grey: #8a8a8a;
    --white: #ffffff;
  }
  * { margin: 0; padding: 0; box-sizing: border-box; }
  html, body { width: 1200px; height: 1200px; overflow: hidden; }
  body { background: var(--stage); position: relative; }

  .cover {
    position: absolute; left: 240px; top: 60px;
    width: 720px; height: 1080px;
    background: var(--paper);
    overflow: hidden;
    box-shadow: 0 18px 40px rgba(0,0,0,.18);
  }
  .cover-shapes { position: absolute; inset: 0; }

  .title {
    position: absolute; left: 48px; top: 44px; width: 640px;
    font-family: "Luckiest Guy", "Montserrat", sans-serif;
    font-size: 62px; line-height: 1.02; letter-spacing: 1px;
    color: var(--teal);
    text-transform: uppercase;
  }
  .subtitle {
    position: absolute; left: 48px; top: 258px; width: 600px;
    font-family: "Montserrat", sans-serif; font-weight: 500;
    font-size: 22px; line-height: 1.25; letter-spacing: .5px;
    color: var(--grey); text-transform: uppercase;
  }
  .endorsement {
    position: absolute; left: 48px; top: 712px; width: 640px;
    font-family: "Jost", sans-serif; font-style: italic;
    font-size: 20px; line-height: 1.3; color: var(--ink);
  }
  .endorsement cite { display: block; font-style: italic; font-weight: 600; }
  .author {
    position: absolute; left: 0; right: 0; top: 990px; text-align: center;
    font-family: "Montserrat", sans-serif; font-weight: 600;
    font-size: 34px; letter-spacing: 1px; color: var(--white);
    text-transform: uppercase;
  }
</style>
</head>
<body>
  <div class="cover">
    <svg class="cover-shapes" width="720" height="1080" viewBox="0 0 720 1080">
      <defs>
        <linearGradient id="photoTone" x1="0" y1="0" x2="1" y2="1">
          <stop offset="0" stop-color="#7cc6c9"/>
          <stop offset="1" stop-color="#4aa9ae"/>
        </linearGradient>
      </defs>
      <rect class="top-band" x="0" y="0" width="720" height="14" fill="var(--teal)"/>
      <rect class="photo" x="0" y="340" width="720" height="320" fill="url(#photoTone)"
            role="img" aria-label="Photograph of young people standing and walking by a wall, looking at their phones, tinted teal"/>
      <polygon class="play-arrow" points="330,410 330,640 540,525" fill="var(--white)" opacity=".85"/>
      <polygon class="accent-strip" points="0,640 720,640 720,700 0,670" fill="var(--teal)"/>
      <polygon class="lower-field" points="0,850 720,990 720,1080 0,1080" fill="var(--teal)"/>
    </svg>

    <h1 class="title">The Nine Gates<br>for Tablet<br>Reliance</h1>
    <p class="subtitle">An Inner Journey to<br>Balanced Tablet Habits</p>

    <blockquote class="endorsement">
      If you suffer from digital addiction, I strongly encourage you to use this book as your road map to get you back to the real world.”
      <cite>-- Thomas Quillard, Founder of Online Channel Monitor.</cite>
    </blockquote>

    <p class="author">Jonas Segrell</p>
  </div>
</body>
</html>
```